PTA Business Card

Seeking design for a business card, standard size. It is going to be for myself in regards to PTA - details:

Hollis Brantley Elementary School
PTA President
Peter Lund
563-555-0147
Lundy1984@mailbarn.example

Requirement:
Facebook icon? "Hollis Brantley PTA Rusk"
Twitter thing? I am new to twitter so not sure what to put, here is the link:
https://twitter.example/HBRoversPTA

I was thinking on the front would be a notebook paper background? Not a requirement but was thinking it would look cool?

Total freedom here, let your creativity spread because I don't have any suggestions for design, sorry. Colors of school district are black and yellow.

Backside I am not sure exactly what to put on it.

```html
<!DOCTYPE html>
<html lang="en">
<head>
<meta charset="utf-8">
<title>Hollis Brantley PTA – Business Card</title>
<link rel="stylesheet" href="https://fonts.googleapis.com/css2?family=PT+Sans:wght@400;700&display=swap">
<style>
  :root {
    --page-bg: #ececea;
    --card-white: #fdfdfb;
    --ink: #141414;
    --school-yellow: #f7e51e;
    --title-yellow: #f2d81a;
    --rule-blue: #b9cde0;
    --sketch-grey: #d8d8d4;
    --shadow: rgba(0, 0, 0, 0.18);
  }
  * { box-sizing: border-box; margin: 0; padding: 0; }
  html, body {
    width: 1200px; height: 720px; overflow: hidden;
    background: var(--page-bg);
    font-family: "PT Sans", Arial, sans-serif;
    color: var(--ink);
  }
  .canvas { position: relative; width: 1200px; height: 720px; }

  .card {
    position: absolute; top: 205px;
    width: 540px; height: 309px;
    box-shadow: 0 6px 18px var(--shadow);
    overflow: hidden;
  }

  /* Front: contact side */
  .card-front { left: 40px; background: var(--card-white); }
  .front-logo { position: absolute; left: 26px; top: 24px; width: 230px; }
  .front-logo .kids-art {
    display: block; margin-left: 70px; width: 110px; height: 34px;
    background: linear-gradient(90deg, var(--sketch-grey), #e8e8e4);
    border-radius: 4px;
  }
  .front-logo .school-name { font-size: 13px; margin-top: 4px; letter-spacing: 0.3px; }

  .contact { position: absolute; left: 250px; top: 118px; }
  .contact .person-name { font-size: 36px; line-height: 1; letter-spacing: 0.5px; text-transform: uppercase; }
  .contact .role { font-size: 17px; font-weight: 700; color: var(--title-yellow); margin: 3px 0 12px 4px; }
  .contact .detail { font-size: 15px; line-height: 1.45; margin-left: 4px; }

  .social-band {
    position: absolute; left: 0; right: 0; bottom: 0; height: 40px;
    background: var(--school-yellow);
    display: flex; align-items: center; justify-content: space-between;
    padding: 0 22px;
  }
  .social { display: flex; align-items: center; gap: 7px; font-size: 14px; }
  .social .mark { width: 14px; height: 14px; background: var(--ink); border-radius: 2px; }

  /* Back: lined notebook side */
  .card-back {
    left: 620px;
    background:
      repeating-linear-gradient(to bottom, transparent 0 18px, var(--rule-blue) 18px 19.5px),
      var(--card-white);
  }
  .back-logo { position: absolute; left: 0; right: 0; top: 48px; text-align: center; }
  .back-logo .kids-art {
    display: block; margin: 0 auto 0 230px; width: 220px; height: 56px;
    background: linear-gradient(90deg, var(--sketch-grey), #e6e6e2);
    border-radius: 6px;
  }
  .back-logo .school-name { font-size: 29px; margin-top: 16px; letter-spacing: 0.5px; }
  .back-logo .underline { display: block; width: 480px; height: 16px; margin: -4px auto 0; }
</style>
</head>
<body>
<main class="canvas">

  <section class="card card-front" aria-label="Business card front">
    <div class="front-logo">
      <span class="kids-art" role="img" aria-label="Sketch of children holding hands"></span>
      <p class="school-name">Hollis Brantley Elementary School</p>
    </div>
    <div class="contact">
      <h1 class="person-name">Peter Lund</h1>
      <p class="role">PTA President</p>
      <p class="detail">563-555-0147</p>
      <p class="detail">Lundy1984@mailbarn.example</p>
    </div>
    <div class="social-band">
      <span class="social"><span class="mark"></span>Hollis Brantley PTA</span>
      <span class="social"><span class="mark"></span>HBRoversPTA</span>
    </div>
  </section>

  <section class="card card-back" aria-label="Business card back">
    <div class="back-logo">
      <span class="kids-art" role="img" aria-label="Sketch of children holding hands"></span>
      <p class="school-name">Hollis Brantley Elementary School</p>
      <svg class="underline" viewBox="0 0 480 16" aria-hidden="true">
        <path d="M4 6 Q240 2 476 13" fill="none" stroke="var(--school-yellow)" stroke-width="4" stroke-linecap="round"/>
      </svg>
    </div>
  </section>

</main>
</body>
</html>
```